Bluegate Wound Care and Hyperbarics Website Refresh

I want to revamp my current website to be more streamlined and look cleaner. I am also adding additional service lines and another location to the company so I would like that added as well. I want to stick with the same logo and colors, but just have it cleaned up with a better overall design.

www.bghyperbarics-example.com

Target Market(s)

Wound Care and Hyperbaric Patients

Industry/Entity Type

Healthcare

Coding

Coded - Design and coding required

Number of Pages Required

5+ page

Colors
0054AA
0677BA
7BADD7
CADEEF
E8F1F8
59FF00
82FF00
B8FF75
E3FFCB
F4FFEA

```html
<!DOCTYPE html>
<html lang="en">
<head>
<meta charset="utf-8">
<title>Bluegate Wound Care and Hyperbarics – Schedule a Consult</title>
<link href="https://fonts.googleapis.com/css2?family=Source+Sans+3:wght@400;600;700&display=swap" rel="stylesheet">
<style>
:root{
  --header-dim:#4f4f4f;
  --header-text:#262626;
  --band-dim:#2b2b2b;
  --page-dim:#4a4a4a;
  --page-text-dim:#232323;
  --accent-green:#6abf2a;
  --accent-green-dim:#3a5d1e;
  --panel:#f3f5f6;
  --field:#ffffff;
  --field-line:#e2e6e8;
  --heading:#2b2b2b;
  --body:#333333;
  --placeholder:#6c6f72;
  --white:#ffffff;
}
*{box-sizing:border-box;margin:0;padding:0}
html,body{width:1200px;height:675px;overflow:hidden}
body{position:relative;background:var(--page-dim);font-family:"Source Sans 3",sans-serif;color:var(--body)}

.site-header{position:absolute;left:0;top:0;width:1200px;height:39px;background:var(--header-dim)}
.brand{position:absolute;left:129px;top:6px;display:flex;align-items:center;gap:5px;color:var(--header-text)}
.brand-dot{width:9px;height:9px;border-radius:50%;background:var(--header-text)}
.brand-name{font-size:15px;font-weight:700;letter-spacing:.5px;line-height:1}
.brand-sub{position:absolute;left:14px;top:18px;font-size:5.5px;font-weight:600;white-space:nowrap}
.main-nav{position:absolute;top:14px;left:641px;display:flex;gap:17px;font-size:8px;font-weight:600;letter-spacing:.6px;color:var(--header-text)}
.main-nav .active{color:#5a4a1e;border-bottom:1px solid #5a4a1e;padding-bottom:2px}
.nav-phone{position:absolute;left:859px;top:14px;font-size:8px;font-weight:600;letter-spacing:.5px;color:var(--header-text);display:flex;gap:6px;align-items:center}
.consult-btn{position:absolute;left:942px;top:9px;width:129px;height:22px;border-radius:11px;background:var(--accent-green-dim);color:#26381a;font-size:7.5px;font-weight:700;letter-spacing:.5px;display:flex;align-items:center;justify-content:center;gap:5px}

.hero-band{position:absolute;left:0;top:39px;width:1200px;height:44px;background:var(--band-dim)}
.slider-dots{position:absolute;left:584px;top:53px;display:flex;gap:6px}
.slider-dots span{width:6px;height:6px;border-radius:50%;border:1px solid #6a6a6a}
.slider-dots span.on{background:#8a8a8a;width:8px;height:8px;margin-top:-1px}

.services-intro{position:absolute;left:0;top:590px;width:1200px;text-align:center}
.eyebrow{font-size:10px;letter-spacing:5px;color:var(--accent-green-dim);font-weight:600}
.section-title{margin-top:12px;font-size:23px;font-weight:600;color:var(--page-text-dim);letter-spacing:.3px}
.section-text{margin-top:10px;font-size:11px;color:var(--page-text-dim);line-height:15px;width:460px;margin-left:auto;margin-right:auto}

.consult-modal{position:absolute;left:64px;top:102px;width:1072px;height:471px;overflow:hidden}
.modal-photo{position:absolute;inset:0;background:linear-gradient(180deg,#7fa9d4 0%,#c9d6e2 30%,#e6e8ea 45%,#7c8a86 60%,#8b6a52 80%,#9a5a45 100%)}
.modal-close{position:absolute;right:9px;top:7px;width:12px;height:12px}
.form-panel{position:absolute;left:561px;top:25px;width:486px;height:421px;background:var(--panel);padding:52px 43px 0}
.form-title{font-size:14.5px;font-weight:600;color:var(--heading);line-height:1}
.form-lead{margin-top:10px;font-size:10.5px;line-height:16.5px;color:var(--body)}
.field{display:block;width:400px;height:28px;background:var(--field);border-bottom:1px solid var(--field-line);margin-top:6px;padding:7px 8px;font-size:9.5px;color:var(--placeholder)}
.field:first-of-type{margin-top:13px;border-bottom-color:var(--accent-green)}
.field.message{height:78px}
.submit-btn{margin-top:24px;width:77px;height:26px;border-radius:13px;background:var(--accent-green);color:var(--white);font-size:7.5px;font-weight:700;letter-spacing:.6px;display:flex;align-items:center;justify-content:center;gap:4px}
</style>
</head>
<body>

<header class="site-header">
  <div class="brand">
    <span class="brand-dot"></span>
    <span class="brand-name">BLUEGATE</span>
    <span class="brand-sub">Wound Care &amp; Hyperbarics</span>
  </div>
  <nav class="main-nav">
    <span>HOME</span><span class="active">ABOUT</span><span>BLOG</span><span>CONTACT US</span>
  </nav>
  <div class="nav-phone">
    <svg width="6" height="8" viewBox="0 0 6 8"><rect x=".5" y=".5" width="5" height="7" rx="1" fill="none" stroke="#262626"/></svg>
    555-014-2288
  </div>
  <div class="consult-btn">
    <svg width="8" height="7" viewBox="0 0 8 7"><rect x=".5" y="1" width="7" height="5.5" fill="none" stroke="#26381a"/></svg>
    SCHEDULE A CONSULT
  </div>
</header>

<div class="hero-band"></div>
<div class="slider-dots"><span></span><span class="on"></span><span></span></div>

<section class="services-intro">
  <p class="eyebrow">USES FOR HBOT</p>
  <h2 class="section-title">HYPERBARIC OXYGEN THERAPY</h2>
  <p class="section-text">Our provider is a board-certified nurse practitioner who is skilled in wound care and family medicine.</p>
</section>

<div class="consult-modal">
  <div class="modal-photo" role="img" aria-label="Aerial photo of a downtown city skyline under a cloudy blue sky"></div>
  <svg class="modal-close" viewBox="0 0 12 12"><path d="M2 2L10 10M10 2L2 10" stroke="#fff" stroke-width="2.2" stroke-linecap="round"/></svg>
  <form class="form-panel">
    <h3 class="form-title">Give us a call to schedule a consult.</h3>
    <p class="form-lead">Lorem Ipsum is simply dummy text of the printing and typesetting industry. Lorem Ipsum has been the industry's standard dummy text ever since the 1500s,</p>
    <span class="field">First Name</span>
    <span class="field">Last Name</span>
    <span class="field">Phone Number</span>
    <span class="field">Your Email</span>
    <span class="field message">How can we help? *</span>
    <div class="submit-btn">
      <svg width="9" height="7" viewBox="0 0 9 7"><rect x=".5" y=".5" width="8" height="6" fill="none" stroke="#fff"/><path d="M.5 .5L4.5 4L8.5 .5" fill="none" stroke="#fff"/></svg>
      SUBMIT
    </div>
  </form>
</div>

</body>
</html>
```